Kelvora Energy Brochure

This will be an 8 page brochure 8.5 X 11" Page Order: Front Cover, Solar, Storage, O&M, Automated Cleaning Systems, Electrical, Roofing, Back Cover. Most information needed can be found on our website. Ask for anything you need.

Target Market(s)

Commercial Solar Customers, Roofing Customers

Industry/Entity Type

Renewable Energy

Font styles to use
Serif

Colors
0054AA
0677BA
7BADD7
CADEEF
E8F1F8

```html
<!DOCTYPE html>
<html lang="en">
<head>
<meta charset="utf-8">
<title>Kelvora Energy Brochure</title>
<link rel="stylesheet" href="https://fonts.googleapis.com/css2?family=Montserrat:ital,wght@0,400;0,500;0,600;0,700;0,800;1,400;1,600&display=swap">
<style>
  :root{
    --navy:#0a4a86;
    --blue:#0054aa;
    --blue-mid:#0677ba;
    --blue-soft:#7badd7;
    --blue-pale:#cadeef;
    --blue-mist:#e8f1f8;
    --green:#6cb33f;
    --paper:#f3f4f6;
    --ink:#3d4650;
    --stage:#dcdddf;
  }
  *{box-sizing:border-box;margin:0;padding:0}
  html,body{width:720px;height:1200px;overflow:hidden}
  body{background:var(--stage);font-family:"Montserrat",sans-serif;color:var(--ink);position:relative}
  .spread{position:absolute;left:20px;width:680px;height:440px;display:flex;box-shadow:0 6px 18px rgba(0,0,0,.18)}
  .spread--covers{top:70px}
  .spread--inside{top:620px}
  .page{position:relative;width:340px;height:440px;overflow:hidden;background:#fff}
  .page svg.shape{position:absolute;inset:0}
  .abs{position:absolute}
  .wordmark{font-weight:800;letter-spacing:-.5px;line-height:1}

  /* front cover */
  .cover{background:var(--paper)}
  .cover .wordmark{left:0;right:0;top:58px;text-align:center;font-size:34px;color:var(--navy)}
  .cover .wordmark span{color:var(--green)}
  .cover-title{left:0;right:0;top:138px;text-align:center;font-size:19px;font-weight:800;color:var(--navy);line-height:1.2}
  .cover-sub{left:0;right:0;top:190px;text-align:center;font-size:9.5px;font-weight:400;color:var(--green);letter-spacing:.5px;line-height:1.3}
  .cover-web{left:0;right:0;bottom:22px;text-align:center;font-size:10px;color:#fff;letter-spacing:2px;font-weight:500}

  /* back cover */
  .back{background:var(--paper)}
  .back .wordmark{left:34px;top:150px;font-size:30px;color:#fff}
  .back .wordmark span{color:var(--green)}
  .contact{left:34px;top:230px;color:#fff}
  .contact .label{font-size:12px;font-weight:500;margin-left:40px}
  .contact .tel{font-size:12px;margin-top:2px}
  .contact .tel b{font-size:22px;font-weight:700}
  .contact .mail{font-size:12px;margin-top:4px}
  .contact .mail b{font-weight:700}
  .contact .web{font-size:10px;letter-spacing:2px;margin-top:6px;font-weight:600}

  /* inside left */
  .panel-title{left:16px;top:150px;width:100px;font-size:13px;font-weight:700;color:#fff;line-height:1.2}
  .panel-text{left:16px;top:210px;width:100px;font-size:7.5px;color:#fff;line-height:1.5}
  .leap{left:140px;top:140px;width:196px;text-align:center}
  .leap h3{font-size:10.5px;font-weight:700;color:var(--navy);line-height:1.2}
  .leap p{font-size:7.5px;color:var(--green);font-style:italic;line-height:1.3;margin-top:2px}
  .feature{width:86px;text-align:center;font-size:6px;line-height:1.35;color:var(--ink)}
  .feature svg{display:block;margin:0 auto 3px}
  .feature--a{left:148px;top:190px}
  .feature--b{left:244px;top:190px}
  .feature--c{left:148px;top:248px}
  .feature--d{left:244px;top:248px}
  .env{left:238px;top:292px;width:94px;font-size:6px;line-height:1.4}
  .env h4{font-size:8px;color:var(--blue-mid);font-weight:600;line-height:1.1;margin-bottom:3px}
  .env p+p{margin-top:4px}
  .benefit{left:16px;width:212px;font-size:6px;line-height:1.45}
  .benefit h4{font-size:9px;color:var(--blue-mid);font-weight:600;margin-bottom:2px;line-height:1.1}
  .benefit--equity{top:304px}
  .benefit--economics{top:364px}

  /* inside right */
  .lead{left:20px;top:20px;width:300px}
  .lead h2{font-size:10px;font-weight:700;color:var(--navy);line-height:1.25}
  .lead p{font-size:7px;color:var(--blue-mid);line-height:1.3;margin-top:4px;text-align:center}
  .col{width:92px;top:98px;font-size:6px;line-height:1.4}
  .col h4{font-size:8px;color:var(--blue-mid);font-weight:600;line-height:1.1;margin-bottom:3px}
  .col p+p{margin-top:4px}
  .col--protect{left:20px}
  .col--savings{left:124px}
  .col--focus{left:228px}
  .partners{left:20px;top:218px;width:300px;font-size:10px;font-weight:700;color:var(--green);text-align:center}
  .ticks{list-style:none;font-size:6.2px;line-height:1.75}
  .ticks li{display:flex;align-items:center;gap:4px}
  .ticks--left{left:26px;top:238px}
  .ticks--right{left:178px;top:238px}
  .cta{left:18px;top:346px;width:168px;color:#fff}
  .cta h3{font-size:9.5px;font-weight:700;line-height:1.25}
  .cta p{font-size:9px;font-style:italic;margin-top:6px;line-height:1.25}
</style>
</head>
<body>

<section class="spread spread--covers">
  <article class="page back">
    <svg class="shape" viewBox="0 0 340 440" aria-hidden="true">
      <defs>
        <linearGradient id="roofPhoto" x1="0" y1="0" x2="1" y2="1">
          <stop offset="0" stop-color="#1f3d2a"/>
          <stop offset=".35" stop-color="#254f82"/>
          <stop offset="1" stop-color="#1c4a86"/>
        </linearGradient>
      </defs>
      <path d="M0,140 C80,95 190,90 260,130 C300,160 330,230 340,300 V440 H0 Z" fill="url(#roofPhoto)" role="img" aria-label="Photo of a large commercial rooftop covered with solar panels beside trees"/>
      <path d="M0,140 C80,95 190,90 260,130 C300,160 330,230 340,300 V440 H0 Z" fill="var(--navy)" opacity=".55"/>
      <circle cx="70" cy="450" r="120" fill="var(--green)"/>
    </svg>
    <div class="abs wordmark">Kelvora <span>Energy</span></div>
    <div class="abs contact">
      <div class="label">Contact Us</div>
      <div class="tel">Tel. <b>555-014-2290</b></div>
      <div class="mail">Email: <b>sales@kelvoraenergy.com</b></div>
      <div class="web">WWW.KELVORAENERGY.COM</div>
    </div>
  </article>

  <article class="page cover">
    <svg class="shape" viewBox="0 0 340 440" aria-hidden="true">
      <defs>
        <linearGradient id="fieldPhoto" x1="0" y1="0" x2="0" y2="1">
          <stop offset="0" stop-color="#c9b6dc"/>
          <stop offset=".3" stop-color="#e8c16a"/>
          <stop offset=".45" stop-color="#7b6fb0"/>
          <stop offset=".75" stop-color="#2f4f9a"/>
          <stop offset="1" stop-color="#5d7a2a"/>
        </linearGradient>
      </defs>
      <rect x="0" y="100" width="340" height="340" fill="url(#fieldPhoto)" role="img" aria-label="Photo of rows of ground-mounted solar panels in a grassy field at sunrise"/>
      <path d="M0,0 H340 V110 C330,250 210,300 110,292 C50,287 15,268 0,252 Z" fill="var(--paper)"/>
      <path d="M340,110 C330,250 210,300 110,292 C50,287 15,268 0,252" fill="none" stroke="var(--navy)" stroke-width="4"/>
    </svg>
    <div class="abs wordmark">Kelvora <span>Energy</span></div>
    <h1 class="abs cover-title">YOUR RENEWABLE<br>ENERGY PARTNER</h1>
    <p class="abs cover-sub">COMPREHENSIVE AND EFFECTIVE<br>RENEWABLE ENERGY SYSTEMS</p>
    <p class="abs cover-web">WWW.KELVORAENERGY.COM</p>
  </article>
</section>

<section class="spread spread--inside">
  <article class="page">
    <svg class="shape" viewBox="0 0 340 440" aria-hidden="true">
      <defs>
        <linearGradient id="panelPhoto" x1="1" y1="0" x2="0" y2="1">
          <stop offset="0" stop-color="#fbe3b0"/>
          <stop offset=".45" stop-color="#4a6fb0"/>
          <stop offset="1" stop-color="#2b4370"/>
        </linearGradient>
      </defs>
      <path d="M0,0 H340 V40 C290,110 160,136 0,122 Z" fill="url(#panelPhoto)" role="img" aria-label="Photo of solar panels glowing in sunlight with flowers in front"/>
      <path d="M0,122 C40,128 84,134 126,134 C140,180 142,250 120,282 C80,292 30,296 0,298 Z" fill="var(--navy)" stroke="var(--green)" stroke-width="3"/>
      <path d="M340,40 C290,110 160,136 0,122" fill="none" stroke="#fff" stroke-width="3"/>
      <path d="M0,428 C120,424 250,414 340,396 V440 H0 Z" fill="var(--green)"/>
      <path d="M0,434 C120,431 250,424 340,408 V440 H0 Z" fill="var(--navy)"/>
    </svg>
    <h2 class="abs panel-title">Transform Your Energy Management</h2>
    <p class="abs panel-text">Reduce your business's operating costs by exploring solar and energy storage solutions.</p>
    <div class="abs leap">
      <h3>Taking the leap to solar can<br>seem stressful.</h3>
      <p>Your business deserves a stress-free, simple,<br>and secure experience</p>
    </div>
    <div class="abs feature feature--a">
      <svg width="18" height="18" viewBox="0 0 20 20"><circle cx="10" cy="10" r="10" fill="var(--blue-mid)"/><circle cx="10" cy="9" r="3.5" fill="none" stroke="#fff" stroke-width="1.2"/><path d="M8.5,13h3M9,15h2" stroke="#fff" stroke-width="1.2"/></svg>
      Serving all of northern california - and beyond
    </div>
    <div class="abs feature feature--b">
      <svg width="18" height="18" viewBox="0 0 20 20"><circle cx="10" cy="10" r="10" fill="var(--blue-mid)"/><path d="M6,11l6-3v6z" fill="#fff"/></svg>
      Licensed and bonded in general structural contracting, electrical contracting and roofing contracting
    </div>
    <div class="abs feature feature--c">
      <svg width="18" height="18" viewBox="0 0 20 20"><circle cx="10" cy="10" r="10" fill="var(--blue-mid)"/><path d="M6,14l7-7 1.5,1.5-7,7H6z" fill="#fff"/></svg>
      High quality resources made in the usa
    </div>
    <div class="abs feature feature--d">
      <svg width="18" height="18" viewBox="0 0 20 20"><circle cx="10" cy="10" r="10" fill="var(--blue-mid)"/><rect x="5" y="6" width="8" height="6" rx="2" fill="#fff"/><rect x="8" y="9" width="7" height="5" rx="2" fill="none" stroke="#fff"/></svg>
      Customer support is our top priority
    </div>
    <div class="abs env">
      <h4>Environmental Impact</h4>
      <p>It's no secret that solar lessens your reliance on other forms of energy and reduces your carbon footprint.</p>
      <p>A big benefit of solar panels for businesses is that they can build trust among your customers by showing your commitment to sustainable energy.</p>
    </div>
    <div class="abs benefit benefit--equity">
      <h4>Increase Business Equity</h4>
      <p>Many studies prove that solar panels can be more valuable and increase the property value of homes and commercial buildings than those that don't, and that trend is unlikely to change anytime soon. The commercial solar revolution is becoming increasingly popular and adding solar panels to your building will make it more desirable.</p>
    </div>
    <div class="abs benefit benefit--economics">
      <h4>Improve Economics</h4>
      <p>Solar can reduce your overall operating cost by as much as 30%. Kelvora Energy helps businesses maximize solar savings so you can reinvest in, grow, and differentiate your business.</p>
    </div>
  </article>

  <article class="page">
    <svg class="shape" viewBox="0 0 340 440" aria-hidden="true">
      <defs>
        <linearGradient id="bandPhoto" x1="0" y1="0" x2="1" y2="0">
          <stop offset="0" stop-color="#3c3f45"/>
          <stop offset=".6" stop-color="#55606e"/>
          <stop offset="1" stop-color="#3a5f8f"/>
        </linearGradient>
        <linearGradient id="cityPhoto" x1="0" y1="0" x2="0" y2="1">
          <stop offset="0" stop-color="#f2c48c"/>
          <stop offset=".5" stop-color="#9fc3e8"/>
          <stop offset="1" stop-color="#3f6fb0"/>
        </linearGradient>
      </defs>
      <path d="M0,336 C120,332 240,320 340,300 V440 H0 Z" fill="url(#bandPhoto)" role="img" aria-label="Photo of a rooftop solar array under a grey sky"/>
      <path d="M0,336 C120,332 240,320 340,300" fill="none" stroke="var(--green)" stroke-width="3"/>
      <circle cx="244" cy="372" r="44" fill="url(#cityPhoto)" stroke="#fff" stroke-width="4" role="img" aria-label="Photo of solar panels overlooking a city skyline at dusk"/>
    </svg>
    <div class="abs lead">
      <h2>Businesses are realizing that keeping their solar system well maintained and efficient is vital to the bottom line.</h2>
      <p>You will experience an easy, to-the-point process while being guided by a highly trusted and experienced team.</p>
    </div>
    <div class="abs col col--protect">
      <h4>Protect Your Energy Assets</h4>
      <p>With your maintenance plan, you can be assured that your investment is kept in good shape and producing 100%. This consistency in production over time ensures a positive return on investment.</p>
    </div>
    <div class="abs col col--savings">
      <h4>Maintain Energy Savings</h4>
      <p>It is crucial to keep an energy-efficient solar system maintained after installation and to optimize it to offer maximum savings.</p>
      <p>There are many things we can do to assure your system operates at the highest efficiency, such as regular cleaning, performance monitoring, removing debris, etc.</p>
    </div>
    <div class="abs col col--focus">
      <h4>Focus On Your Business</h4>
      <p>Managing your energy systems is not your primary function when you're an owner or manager.</p>
      <p>You can trust us to take care of your energy systems, saving you money and time and allowing you more time to grow and manage your business.</p>
    </div>
    <h3 class="abs partners">Consider us your long-term energy partners.</h3>
    <ul class="abs ticks ticks--left">
      <li><svg width="7" height="7" viewBox="0 0 8 8"><circle cx="4" cy="4" r="3.5" fill="none" stroke="var(--blue-mid)" stroke-width=".8"/><path d="M2.3,4l1.2,1.2 2.3-2.4" fill="none" stroke="var(--blue-mid)" stroke-width=".8"/></svg>Corrective and Scheduled Maintenance</li>
      <li><svg width="7" height="7" viewBox="0 0 8 8"><circle cx="4" cy="4" r="3.5" fill="none" stroke="var(--blue-mid)" stroke-width=".8"/><path d="M2.3,4l1.2,1.2 2.3-2.4" fill="none" stroke="var(--blue-mid)" stroke-width=".8"/></svg>Condition-based Maintenance</li>
      <li><svg width="7" height="7" viewBox="0 0 8 8"><circle cx="4" cy="4" r="3.5" fill="none" stroke="var(--blue-mid)" stroke-width=".8"/><path d="M2.3,4l1.2,1.2 2.3-2.4" fill="none" stroke="var(--blue-mid)" stroke-width=".8"/></svg>Performance Optimization</li>
      <li><svg width="7" height="7" viewBox="0 0 8 8"><circle cx="4" cy="4" r="3.5" fill="none" stroke="var(--blue-mid)" stroke-width=".8"/><path d="M2.3,4l1.2,1.2 2.3-2.4" fill="none" stroke="var(--blue-mid)" stroke-width=".8"/></svg>24/7 System Monitoring</li>
    </ul>
    <ul class="abs ticks ticks--right">
      <li><svg width="7" height="7" viewBox="0 0 8 8"><circle cx="4" cy="4" r="3.5" fill="none" stroke="var(--blue-mid)" stroke-width=".8"/><path d="M2.3,4l1.2,1.2 2.3-2.4" fill="none" stroke="var(--blue-mid)" stroke-width=".8"/></svg>Regular Site Visits</li>
      <li><svg width="7" height="7" viewBox="0 0 8 8"><circle cx="4" cy="4" r="3.5" fill="none" stroke="var(--blue-mid)" stroke-width=".8"/><path d="M2.3,4l1.2,1.2 2.3-2.4" fill="none" stroke="var(--blue-mid)" stroke-width=".8"/></svg>Automated Cleaning Solutions</li>
      <li><svg width="7" height="7" viewBox="0 0 8 8"><circle cx="4" cy="4" r="3.5" fill="none" stroke="var(--blue-mid)" stroke-width=".8"/><path d="M2.3,4l1.2,1.2 2.3-2.4" fill="none" stroke="var(--blue-mid)" stroke-width=".8"/></svg>Remote Diagnostics &amp; Power Operation</li>
      <li><svg width="7" height="7" viewBox="0 0 8 8"><circle cx="4" cy="4" r="3.5" fill="none" stroke="var(--blue-mid)" stroke-width=".8"/><path d="M2.3,4l1.2,1.2 2.3-2.4" fill="none" stroke="var(--blue-mid)" stroke-width=".8"/></svg>48 Hour Emergency Response</li>
    </ul>
    <div class="abs cta">
      <h3>Are you ready to take solar panel maintenance off of your to-do list?</h3>
      <p>Need an O&amp;M Consultation?</p>
    </div>
  </article>
</section>

</body>
</html>
```